Etiketten-Design für Produkte eines Familienbetriebs mit Imkerei und Hühnerhaltung
Zielgruppe
Wir sind ein Familienbetrieb mit Imkerei und Hühnerhaltung. Wir suchen für unsere Produkte ein modernes Corporate Design, mit zentralen, bei jedem Produkt vorkommenden Elementen, sowie Elementen, welche produktindividuell sind.
Wir leben in einem 150 jährigen Riegelhaus, welches in der Umgebung sehr bekannt ist. Es soll im Etiketten-Design zentral erscheinen.
Unsere Produkte sind: Honig, Pollen, Eier
Aufgabenstellung
1. Zentrale, auf allen Etiketten wiederkehrende Elemente:
- Unser Riegelhaus (stilisiert) (Bild beiliegend)
- Das Wort 'Birkeneck' (Anmerkung: ohne Anführungszeichen)
- die zentralen Elemente sollen die Produkte nicht überragen.
2. Dezente Adresse:
- Familie Dorbach, Birkeneck, CH-9573 Holtikon
3. Produkte:
a) Honig
Sorten: Waldhonig (dunkel), Blütenhonig (gelblich-goldig), Crèmehonig (gelblich-weisslich), Lavendelhonig (gelblich-goldig)
Die Honigsorten sollen farblich hervortreten.
Freifeld (zweizeilig): für die Lotnummer und die Haltbarkeitsangabe)
Gewicht: 250 g, 500 g
b) Pollen
Gewicht: 100 g
c) Eier
Verpackungseinheiten: 4er-, 6er-, 10er-Packung
Haltungsform: BIO-Haltung
das Wort 'frisch'
Farbe grün (=Bio) soll farblich hervortreten (ähnlich wie beim Honig)
Freifeld (zweizeilig: für das Eigewicht und die Haltbarkeitsangabe)
Bitte keine Stock-Bilder verwenden. Die Etiketten sollen schlicht, edel ,schörkellos und modern erscheinen.
Das Etikett soll Exklusivität und Qualität ausstrahlen. Etikettenhintergrund einfarbig.
Interessanterweise gibt es bei Weinen solche Etiketten. Ich habe einige rausgesucht und angehängt, um die Richtung vorzugeben. (Wein1-6)
Ich habe auch eine schlichte Honigetikette gefunden, die ins Schema passt. (Imker1)
Zusätzlich sind jetzt auch noch Farbbeispiele der Honigsorten zur besseren Abstimmung von Inhalt und Etikette beigelegt. Lavendelhonig ist dem Blütenhonig sehr ähnlich.
Etikettengrössen:
Honig/Pollen 250 g: 190 x 42 mm
Honig 500 g: 206 x 45 mm
Eier 4er: 60 x 60 mm
Eier 6er: 110 x 60 mm
Eier 10er: 170 x 60 cm

```html
<!DOCTYPE html>
<html lang="de">
<head>
<meta charset="utf-8">
<title>Waldhonig – Birkeneck</title>
<link rel="stylesheet" href="https://fonts.googleapis.com/css2?family=Poppins:wght@600;700&family=Oswald:wght@500;600&family=Josefin+Sans:wght@300;400&display=swap">
<style>
  :root {
    --bg: #141619;
    --gold: #e2c178;
    --stone: #c9c6b8;
    --text-light: #cfccc2;
    --sky: #e9ecef;
    --plaster: #f1efe9;
    --timber: #8a3a24;
    --lawn: #4e7a3c;
  }
  * { margin: 0; padding: 0; box-sizing: border-box; }
  html, body { width: 1200px; height: 800px; overflow: hidden; background: var(--bg); }
  .canvas { position: relative; width: 1200px; height: 800px; background: var(--bg); }
  .frames { position: absolute; inset: 0; }
  .line { position: absolute; left: 0; width: 1200px; text-align: center; }
  .category {
    top: 50px; font-family: "Poppins", sans-serif; font-weight: 600;
    font-size: 37px; line-height: 1; letter-spacing: 9px; color: var(--stone);
    padding-left: 9px;
  }
  .variety {
    top: 96px; font-family: "Poppins", sans-serif; font-weight: 700;
    font-size: 64px; line-height: 1; letter-spacing: 17px; color: var(--gold);
    padding-left: 17px;
  }
  .details {
    position: absolute; top: 178px; left: 356px; width: 486px;
    display: flex; justify-content: space-between; align-items: baseline;
  }
  .detail { display: flex; align-items: baseline; gap: 16px; }
  .detail-label {
    font-family: "Josefin Sans", sans-serif; font-weight: 300;
    font-size: 19px; letter-spacing: 1px; color: var(--text-light);
  }
  .detail-value {
    font-family: "Oswald", sans-serif; font-weight: 500;
    font-size: 30px; letter-spacing: 1px; color: var(--gold);
  }
  .detail-lot { gap: 8px; }
  .farmhouse {
    position: absolute; left: 382px; top: 279px; width: 440px; height: 290px;
    background:
      linear-gradient(180deg, var(--sky) 0%, var(--sky) 28%, var(--timber) 30%, #b86a54 45%, var(--plaster) 62%, #ddd6c8 88%, var(--lawn) 94%, #3e6530 100%);
  }
  .address {
    top: 622px; font-family: "Josefin Sans", sans-serif; font-weight: 300;
    font-size: 15px; letter-spacing: 1.2px; color: var(--text-light);
  }
  .brand {
    top: 650px; font-family: "Oswald", sans-serif; font-weight: 600;
    font-size: 46px; line-height: 1.2; letter-spacing: 2px; color: var(--gold);
  }
  .weight {
    top: 720px; font-family: "Poppins", sans-serif; font-weight: 600;
    font-size: 19px; letter-spacing: 6px; color: var(--text-light);
    padding-left: 6px;
  }
</style>
</head>
<body>
<main class="canvas">
  <svg class="frames" width="1200" height="800" viewBox="0 0 1200 800" aria-hidden="true">
    <g fill="none" stroke="#e2c178">
      <rect class="frame-outer" x="295" y="30" width="610" height="741" stroke-width="3"/>
      <rect class="frame-inner" x="304" y="39" width="591" height="723" stroke-width="1.2"/>
      <polygon class="photo-frame-outer" points="360,265 600,247 839,265 839,585 600,603 360,585" stroke-width="3"/>
      <polygon class="photo-frame-inner" points="369,274 600,256 830,274 830,576 600,594 369,576" stroke-width="1.5"/>
    </g>
  </svg>

  <div class="line category">HONIG</div>
  <h1 class="line variety">WALDHONIG</h1>

  <div class="details">
    <div class="detail">
      <span class="detail-label">Farblich</span>
      <span class="detail-value">12/01/19</span>
    </div>
    <div class="detail detail-lot">
      <span class="detail-label">Lotnummer</span>
      <span class="detail-value">1234</span>
    </div>
  </div>

  <div class="farmhouse" role="img" aria-label="Fotografie des Riegelhauses mit rotem Fachwerk, grünen Fensterläden und Baum vor hellem Himmel"></div>

  <p class="line address">Familie Dorbach, Birkeneck, CH-9573 Holtikon</p>
  <p class="line brand">BIRKENECK</p>
  <p class="line weight">250G</p>
</main>
</body>
</html>
```